Fundlark project image

I need a image created that will be the forward face of our Fundlark campaign. Our project is a Linkwave programmable led dog collar controlled by a smart phone app that allows you to individually control the LED's on the collar. It includes solid color, strobe, and fade effects. The resolution needs to be at least 640x by 480x and be 4:3 aspect ratio as this what is required by Fundlark. I uploaded a few pictures of the prototypes and app. These do not have to be included in the image you create and are just to give you an idea of the product. The rest I leave to you, use your imagination and go nuts :) Thanks.

```html
<!DOCTYPE html>
<html lang="en">
<head>
<meta charset="utf-8">
<title>LED Dog Collar</title>
<link rel="stylesheet" href="https://fonts.googleapis.com/css2?family=Josefin+Sans:wght@300;400&display=swap">
<style>
  :root {
    --bg-deep: #0b0b0c;
    --bg-mid: #1c1c1e;
    --bg-glow: #3a3a3c;
    --ink: #ffffff;
    --ink-soft: #ececec;
    --photo-dark: #1a1b20;
    --photo-mid: #6c7078;
    --photo-light: #d9dbe0;
    --collar: #43d3f2;
  }
  html, body {
    margin: 0;
    padding: 0;
    overflow: hidden;
    background: var(--bg-deep);
  }
  .poster {
    position: relative;
    width: 1200px;
    height: 900px;
    overflow: hidden;
    background:
      radial-gradient(ellipse 900px 700px at 780px 180px, var(--bg-glow) 0%, var(--bg-mid) 45%, var(--bg-deep) 100%);
    font-family: "Josefin Sans", sans-serif;
    color: var(--ink);
  }
  .dog-photo {
    position: absolute;
    left: 0;
    top: 20px;
    width: 470px;
    height: 880px;
    border-radius: 200px 200px 0 0;
    background:
      linear-gradient(180deg, transparent 0 250px, rgba(67,211,242,0.55) 265px 320px, transparent 335px),
      linear-gradient(180deg, var(--photo-dark) 0%, var(--photo-mid) 35%, var(--photo-light) 60%, var(--photo-mid) 100%);
    opacity: 0.9;
  }
  .headline {
    position: absolute;
    left: 505px;
    top: 106px;
    margin: 0;
    font-weight: 300;
    font-size: 46px;
    letter-spacing: 4px;
    line-height: 1;
  }
  .copy {
    position: absolute;
    left: 506px;
    top: 184px;
    width: 680px;
    font-weight: 300;
    font-size: 29px;
    line-height: 36px;
    letter-spacing: 2px;
    color: var(--ink-soft);
  }
  .copy p { margin: 0 0 28px; }
  .features {
    position: absolute;
    left: 585px;
    top: 662px;
    display: flex;
    gap: 58px;
    list-style: none;
    margin: 0;
    padding: 0;
  }
  .feature {
    width: 162px;
    display: flex;
    flex-direction: column;
    align-items: center;
  }
  .feature-icon {
    width: 127px;
    height: 127px;
    border: 3px solid var(--ink);
    border-radius: 26px;
    display: flex;
    align-items: center;
    justify-content: center;
  }
  .feature-label {
    margin-top: 30px;
    font-size: 24px;
    line-height: 30px;
    letter-spacing: 1px;
    text-align: center;
  }
</style>
</head>
<body>
<main class="poster">
  <div class="dog-photo" role="img" aria-label="Photo of a husky standing and wearing a glowing blue LED collar"></div>

  <h1 class="headline">LED DOG COLLAR</h1>

  <div class="copy">
    <p>Linkwave programmable led dog collar<br>controlled by a smart phone app.</p>
    <p>individuall LED control on the collar.<br>It includes solid color, strobe, and fade<br>effects.</p>
  </div>

  <ul class="features">
    <li class="feature">
      <div class="feature-icon">
        <svg width="70" height="100" viewBox="0 0 70 100" aria-hidden="true">
          <path d="M10 30 A25 25 0 0 1 60 30 V68 H10 Z" fill="#fff"/>
          <rect x="4" y="66" width="62" height="8" fill="#fff"/>
          <rect x="20" y="74" width="5" height="24" fill="#fff"/>
          <rect x="45" y="74" width="5" height="20" fill="#fff"/>
        </svg>
      </div>
      <span class="feature-label">LED</span>
    </li>
    <li class="feature">
      <div class="feature-icon">
        <svg width="54" height="96" viewBox="0 0 54 96" aria-hidden="true">
          <rect x="2" y="2" width="50" height="92" rx="10" fill="none" stroke="#fff" stroke-width="4"/>
          <rect x="10" y="12" width="34" height="28" rx="2" fill="#fff"/>
          <g fill="#fff">
            <rect x="10" y="48" width="8" height="6" rx="1"/><rect x="23" y="48" width="8" height="6" rx="1"/><rect x="36" y="48" width="8" height="6" rx="1"/>
            <rect x="10" y="59" width="8" height="6" rx="1"/><rect x="23" y="59" width="8" height="6" rx="1"/><rect x="36" y="59" width="8" height="6" rx="1"/>
            <rect x="10" y="70" width="8" height="6" rx="1"/><rect x="23" y="70" width="8" height="6" rx="1"/><rect x="36" y="70" width="8" height="6" rx="1"/>
            <rect x="10" y="81" width="8" height="6" rx="1"/><rect x="23" y="81" width="8" height="6" rx="1"/><rect x="36" y="81" width="8" height="6" rx="1"/>
          </g>
        </svg>
      </div>
      <span class="feature-label">Smart phone<br>controll</span>
    </li>
    <li class="feature">
      <div class="feature-icon">
        <svg width="60" height="60" viewBox="0 0 60 60" aria-hidden="true">
          <circle cx="30" cy="30" r="26" fill="#fff"/>
        </svg>
      </div>
      <span class="feature-label">Linkwave</span>
    </li>
  </ul>
</main>
</body>
</html>
```